Business Card Design for a Sound engineer and DJ

We would like a residn of the business card.

Logo must remain the same.
The card is for the owner of the company.
The business card is in Arabic as the company is based in Kuwait.
The company specializes in sound engineering for singers concerts and events and in addition DJ.
The color options is up to the designer but we would like it masculine as the owner is a man.

Target Market(s)

All ages

Industry/Entity Type

Media

Contact Information for Business Card

Name:
Eng. Tarek Halabi
م/طارق حلبي

The name above is in Arabic and English.

Title: General Manager
Mobile: +965 66307852
Office: +965 22486037
Email: info@sawtarin.net

Address:
Office no. 3
1st floor
Almarfa Complex
Rashed AlQeblawi St.
Salmiya
Kuwait

Instagram: @sawtarin
Snap: sawtarin

Requirements
Nice to have
• can we have Instagram icon and snap icon and a phone vector and email?
• Instead of writing the words

```html
<!DOCTYPE html>
<html lang="en">
<head>
<meta charset="utf-8">
<title>Sawtarin – Business Card</title>
<link href="https://fonts.googleapis.com/css2?family=Roboto:wght@400;500&family=Cairo:wght@500&display=swap" rel="stylesheet">
<style>
  :root {
    --bg: #3a2a22;
    --card-top: #1c1b1e;
    --card-bottom: #050506;
    --violet: #b070e6;
    --pink: #e04fb8;
    --brand: #c47ad8;
    --text: #c9c9cf;
    --muted: #a9a9b0;
  }
  * { margin: 0; padding: 0; box-sizing: border-box; }
  html, body { width: 1200px; height: 900px; overflow: hidden; }
  body {
    background: var(--bg);
    font-family: "Roboto", Arial, sans-serif;
    display: flex; align-items: center; justify-content: center; gap: 40px;
  }
  .card {
    width: 540px; height: 308px; border-radius: 22px;
    background: linear-gradient(160deg, var(--card-top), var(--card-bottom) 70%);
    box-shadow: 0 18px 40px rgba(0,0,0,.55);
    position: relative; color: var(--text);
  }
  .brand { display: flex; align-items: center; gap: 12px; }
  .brand-mark { width: 16px; height: 16px; background: var(--brand); }
  .brand-name { color: var(--brand); font-weight: 500; letter-spacing: .32em; }
  .card-front { display: flex; align-items: center; justify-content: center; }
  .card-front .brand-name { font-size: 30px; }
  .card-back .brand { position: absolute; top: 34px; right: 34px; }
  .card-back .brand-mark { width: 11px; height: 11px; }
  .card-back .brand-name { font-size: 19px; }
  .identity { position: absolute; left: 36px; top: 108px; }
  .name-en { color: var(--violet); font-size: 21px; font-weight: 500; }
  .name-ar { color: var(--pink); font-family: "Cairo", sans-serif; font-size: 20px; line-height: 1.2; direction: rtl; text-align: left; }
  .role { color: var(--muted); font-size: 13px; margin-top: 2px; }
  .address { position: absolute; left: 36px; top: 196px; font-size: 12px; line-height: 1.45; color: var(--muted); }
  .contacts { position: absolute; left: 36px; top: 236px; list-style: none; font-size: 12.5px; line-height: 19px; }
  .contacts li, .socials li { display: flex; align-items: center; gap: 8px; }
  .icon { width: 15px; height: 15px; flex: none; }
  .socials { position: absolute; right: 34px; top: 130px; list-style: none; display: flex; gap: 16px; font-size: 12.5px; }
  .dot { width: 14px; height: 14px; border-radius: 50%; background: var(--pink); flex: none; }
</style>
</head>
<body>
  <section class="card card-front">
    <div class="brand"><span class="brand-mark"></span><span class="brand-name">SAWTARIN</span></div>
  </section>

  <section class="card card-back">
    <div class="brand"><span class="brand-mark"></span><span class="brand-name">SAWTARIN</span></div>

    <div class="identity">
      <p class="name-en">Eng. Tarek Halabi</p>
      <p class="name-ar">م/طارق حلبي</p>
      <p class="role">General Manager</p>
    </div>

    <ul class="socials">
      <li><span class="dot"></span>@sawtarin</li>
      <li><span class="dot"></span>sawtarin</li>
    </ul>

    <p class="address">Office no. 3, 1st floor, Almarfa Complex,<br>Rashed AlQeblawi St., Salmiya, Kuwait</p>

    <ul class="contacts">
      <li>
        <svg class="icon" viewBox="0 0 16 16"><circle cx="8" cy="8" r="8" fill="#e04fb8"/><path d="M5.2 4.2l1.4-.4.8 1.9-.9.7c.4 1 1.1 1.7 2.1 2.1l.7-.9 1.9.8-.4 1.4c-3 .2-5.8-2.6-5.6-5.6z" fill="#111"/></svg>
        +965 22486037
      </li>
      <li>
        <svg class="icon" viewBox="0 0 16 16"><circle cx="8" cy="8" r="8" fill="#e04fb8"/><rect x="5.5" y="3.5" width="5" height="9" rx="1" fill="#111"/><rect x="6.5" y="4.8" width="3" height="5" fill="#e04fb8"/></svg>
        +965 66307852
      </li>
      <li>
        <svg class="icon" viewBox="0 0 16 16"><circle cx="8" cy="8" r="8" fill="#e04fb8"/><rect x="4" y="5" width="8" height="6" fill="#111"/><path d="M4 5l4 3.2L12 5" stroke="#e04fb8" stroke-width="1" fill="none"/></svg>
        info@sawtarin.net
      </li>
    </ul>
  </section>
</body>
</html>
```